UX - Need some screens design for a Skill Assessment Application

I am building an app to carry out skill assessments. Depending on how the assessment is configured, it may have one or more parts
1. Question based assessment (Multiple Choice, True False, Fill in the blanks"
2. Endorsement by two colleagues - A screen that allows user to pick colleagues based on search and shows the status of pending requests
3. A written submission - a page that explains the format of the submission and a file upload
As each assessment can be configured with or without any of the steps, the assessment UI must be such that these areas get hidden/displayed based on configuration.
Colour codes to be used can be #0e78bb and #ffffff
There will also be a start screen (instructions) and an end screen (results)
Target Market(s)
Enterprise software
Number of Pages Required
4 page

```html
<!DOCTYPE html>
<html lang="en"><head><meta charset="utf-8"><title>Assessment Mobile Ver-3</title>
<link href="https://fonts.googleapis.com/css2?family=Inter:wght@400;500;600;700&display=swap" rel="stylesheet">
<style>
:root{--bg:#262626;--brand:#0c5bb5;--brand-2:#1a70c8;--primary:#0e78bb;--teal:#14988c;--ink:#1f2430;--muted:#6b7280;--line:#e3e6eb;--panel:#e8eff6;--note:#f3f4f6;--soft:#f4f5f7;--white:#fff;--chip:#eceef1;--select:#e8f2fb;}
html,body{margin:0;width:1200px;height:681px;overflow:hidden;background:var(--bg)}
.stage{position:absolute;left:0;top:0;width:2568px;height:1456px;transform:scale(.46729);transform-origin:0 0;font-family:Inter,sans-serif;color:var(--ink)}
.title{position:absolute;top:118px;left:0;width:100%;text-align:center;color:var(--white);font-size:25px;font-weight:400;letter-spacing:.3px}
.screen{position:absolute;top:240px;width:275px;background:var(--white);overflow:hidden}
.screen *{box-sizing:border-box}
.abs{position:absolute}
.appbar{position:absolute;left:0;top:0;width:275px;height:80px;background:var(--brand)}
.clock{position:absolute;left:24px;top:9px;color:var(--white);font-size:11px;font-weight:600}
.bar-icons{position:absolute;left:0;top:0}
.avatar{border-radius:50%;background:linear-gradient(160deg,#c9a58b,#5b4a45)}
.me{position:absolute;left:241px;top:44px;width:22px;height:22px;border:1.5px solid var(--white)}
.crumb{position:absolute;left:12px;top:98px;font-size:9.5px;color:var(--muted);display:flex;align-items:center;gap:6px}
.crumb b{font-weight:400;color:var(--primary)}
.crumb svg{margin-right:7px}
.head{position:absolute;left:12px;top:126px;width:251px;display:flex}
.head h1{margin:0 0 0 12px;font-size:15.5px;line-height:19px;font-weight:600;flex:1}
.head .pct{font-size:17px;font-weight:600;align-self:flex-end;margin-bottom:-2px}
.head .pct small{font-size:8px}
.meter{position:absolute;left:0;top:177px;width:275px;height:4px;background:#dde3ea}
.meter i{display:block;height:100%;background:var(--teal)}
.info{position:absolute;left:0;top:181px;width:275px;height:99px;background:var(--panel);padding:14px 11px 0;font-size:8.3px;line-height:20px}
.info span{color:var(--primary)}
.stepper{position:absolute;left:0;top:305px;width:275px;display:flex;justify-content:center;align-items:center;font-size:9px;gap:4px}
.stepper .dot{width:10px;height:10px;border-radius:50%;border:1px solid #b8bec7;display:inline-block}
.stepper .done{background:var(--teal);border-color:var(--teal)}
.stepper .on{color:var(--primary)}
.stepper .dash{width:12px;height:1px;background:#c5cad2;margin:0 3px}
.section{position:absolute;left:12px;top:340px;width:251px;height:29px;border-bottom:1px solid var(--line);display:flex;justify-content:space-between}
.section h2{margin:0;font-size:12.5px;font-weight:600}
.save{font-size:9px;color:var(--primary);display:flex;gap:6px;align-items:flex-start;padding-top:4px}
.field{position:absolute;left:12px;width:251px;height:26px;border:1px solid #d8dce2;border-radius:3px;font-size:8.5px;color:var(--muted);padding:7px 10px;display:flex;justify-content:space-between;align-items:center}
.field.dark{color:var(--ink)}
.send{position:absolute;left:12px;top:453px;width:251px;height:25px;border:1px solid var(--line);border-radius:3px;font-size:9px;color:#a8adb5;text-align:center;line-height:23px}
.send.live{border-color:var(--primary);color:var(--primary)}
.row{position:absolute;left:12px;width:251px;height:34px;border:1px solid var(--line);border-radius:3px;display:flex;align-items:center;padding-left:6px}
.box{width:11px;height:11px;border:1px solid #c5cad2;border-radius:2px;margin-right:8px;flex:none}
.box.on{background:var(--primary);border-color:var(--primary);position:relative}
.box.on:after{content:"";position:absolute;left:3px;top:0.5px;width:3px;height:6px;border:solid #fff;border-width:0 1.5px 1.5px 0;transform:rotate(45deg)}
.row .avatar{width:22px;height:22px;margin-right:10px;flex:none}
.who{flex:1;font-size:9.5px;font-weight:500;line-height:11px}
.who small{display:block;font-size:8px;font-weight:400;color:var(--muted)}
.add{width:37px;height:20px;background:var(--primary);color:#fff;font-size:9px;border-radius:3px;text-align:center;line-height:20px;margin-right:6px;font-weight:500}
.actions{position:absolute;left:12px;width:251px;height:26px;display:flex;align-items:center;justify-content:space-between;font-size:9px}
.btn-out{width:61px;height:26px;border:1px solid var(--primary);color:var(--primary);border-radius:3px;text-align:center;line-height:24px}
.btn{width:45px;height:26px;background:var(--primary);color:#fff;border-radius:3px;text-align:center;line-height:26px}
.skip{margin-left:auto;margin-right:22px;color:var(--muted)}
.note{position:absolute;left:12px;width:251px;background:var(--note);padding:18px 17px;font-size:9.5px;line-height:17.5px;color:var(--muted)}
.note h3{margin:0 0 8px;font-size:12.5px;font-weight:500;color:var(--ink)}
.dim{position:absolute;inset:0;background:rgba(20,24,32,.3)}
.modal{position:absolute;left:11px;top:385px;width:252px;height:237px;background:#fff;border-radius:8px;padding:20px 23px}
.modal h4{margin:0;font-size:12.5px;font-weight:600;padding-bottom:12px;border-bottom:1px solid var(--line)}
.progress-line{position:absolute;left:12px;top:384px;width:251px;display:flex;align-items:center;font-size:9.5px;color:var(--muted)}
.progress-line .count{margin-left:6px;font-size:8.5px}
.progress-line svg:first-child{margin-right:6px}
.progress-line .ring{margin-left:auto}
.q{position:absolute;left:12px;width:251px;display:flex;font-size:12.5px;line-height:15.5px;font-weight:500}
.q .no{width:42px;color:#4b5360;font-weight:400}
.opt{position:absolute;left:12px;width:251px;height:52px;border:1px solid var(--line);border-radius:3px;display:flex;align-items:center;padding-left:11px;font-size:9.5px;line-height:12px;color:#4b5360}
.opt .n{width:26px;height:24px;background:#e3eefa;color:var(--primary);font-size:11px;text-align:center;line-height:24px;margin-right:19px}
.opt.sel{border:1.5px solid var(--primary);background:var(--select);color:var(--primary)}
.opt.sel .n{background:#cfe2f5}
.pill{position:absolute;top:478px;height:25px;border-radius:13px;font-size:9px;text-align:center;line-height:23px}
.blank-text{position:absolute;left:54px;font-size:12.5px;font-weight:500}
.blank{position:absolute;border-bottom:1px solid var(--line);color:#c1c6cd;font-size:12px;padding-bottom:4px}
/* home */
.hero{position:absolute;left:0;top:0;width:275px;height:316px;background:var(--brand)}
.hello{position:absolute;left:66px;top:87px;color:#fff}
.hello small{display:block;font-size:9.5px;opacity:.75}
.hello strong{display:block;font-size:13.5px;font-weight:600;margin-top:5px}
.create{position:absolute;left:66px;top:133px;width:152px;height:28px;background:var(--brand-2);border-radius:3px;color:#fff;font-size:9px;display:flex;align-items:center;justify-content:center;gap:6px}
.sum-label{position:absolute;left:12px;top:179px;color:#fff;font-size:11px}
.card-blue{position:absolute;top:205px;height:76px;background:#1e6ec4;border-radius:4px}
.soft{position:absolute;left:0;top:316px;width:275px;height:565px;background:var(--soft)}
.tabs{position:absolute;left:12px;top:368px;display:flex;background:var(--chip);border-radius:3px;font-size:9.5px}
.tabs span{padding:0 14px;line-height:26px;color:#4b5360}
.tabs .act{background:var(--primary);color:#fff;border-radius:3px}
.a-card{position:absolute;left:12px;width:251px;height:141px;background:#fff;border-radius:3px;padding:18px 17px;font-size:10px}
.a-card .id{color:#4b5360}
.a-card .name{color:var(--primary);margin-top:9px;font-size:10.5px}
.a-card .dates{display:flex;margin-top:12px;gap:0}
.a-card .dates div{width:107px;font-size:10px;color:#4b5360}
.a-card .dates small{display:block;font-size:7.5px;color:var(--ink);margin-bottom:4px;letter-spacing:.2px}
.chips{display:flex;gap:8px;margin-top:14px}
.chip{background:var(--chip);border-radius:10px;font-size:7.5px;color:#4b5360;padding:0 9px;height:19px;display:flex;align-items:center;gap:4px}
.tick{width:11px;height:11px;border-radius:50%;background:var(--teal);position:relative}
.tick:after{content:"";position:absolute;left:3.8px;top:2px;width:2.4px;height:5px;border:solid #fff;border-width:0 1.3px 1.3px 0;transform:rotate(45deg)}
.kebab{position:absolute;right:14px;top:16px;width:3px}
.kebab i{display:block;width:3px;height:3px;border-radius:50%;background:#4b5360;margin-bottom:2.5px}
</style></head>
<body>
<div class="stage">
<div class="title">Assessment Mobile Ver-3</div>

<!-- Screen: Home -->
<section class="screen" style="left:101px;height:881px">
  <div class="hero"></div>
  <div class="clock">9:41</div>
  <svg class="bar-icons" width="275" height="80" viewBox="0 0 275 80" aria-hidden="true"><g fill="#fff"><rect x="216" y="15" width="2" height="4"/><rect x="219" y="13" width="2" height="6"/><rect x="222" y="11" width="2" height="8"/><rect x="225" y="9" width="2" height="10"/><path d="M230 12a8 8 0 0 1 10 0l-1.3 1.5a6 6 0 0 0-7.4 0zM232.3 14.7a4.5 4.5 0 0 1 5.4 0L235 18z"/><rect x="244" y="11" width="16" height="7" rx="2"/></g><g stroke="#fff" stroke-width="1.5" fill="none" stroke-linecap="round"><path d="M12 50h15M12 55h11M12 60h15"/><path d="M180 60h12M182 60v-5a4 4 0 0 1 8 0v5M185 63h2"/><circle cx="216" cy="55" r="2.5"/><circle cx="216" cy="55" r="6" stroke-dasharray="3 1.8"/></g></svg>
  <div class="avatar me" role="img" aria-label="User profile photo"></div>
  <div class="avatar abs" role="img" aria-label="User profile photo" style="left:12px;top:84px;width:36px;height:36px"></div>
  <div class="hello"><small>Welcome back!</small><strong>Mara T. Lindqvist</strong></div>
  <div class="create"><svg width="10" height="10" viewBox="0 0 10 10" fill="none" stroke="#fff" stroke-width="1"><rect x="1" y="1" width="7" height="8" rx="1"/><path d="M3 4h3M3 6h2"/></svg>Create New Assessment</div>
  <div class="sum-label">Summary</div>
  <div class="card-blue" style="left:-12px;width:22px"></div>
  <div class="card-blue" style="left:26px;width:223px">
    <svg class="abs" style="left:16px;top:14px" width="22" height="22" viewBox="0 0 22 22" fill="none" stroke="#fff" stroke-width="1.3"><rect x="1" y="1" width="20" height="20" rx="3" stroke-opacity=".4"/><path d="M6 16h10M8 16v-5l3-3 3 3v5M11 5v2"/></svg>
    <div class="abs" style="left:56px;top:16px;color:#fff;font-size:14px;font-weight:600">3</div>
    <div class="abs" style="left:56px;top:40px;color:#fff;font-size:9.5px">Endorsements</div>
    <div class="abs" style="left:56px;top:55px;color:#fff;font-size:7px;opacity:.75">1 pending</div>
  </div>
  <div class="card-blue" style="left:262px;width:22px"></div>
  <svg class="abs" style="left:115px;top:293px" width="46" height="6" viewBox="0 0 46 6"><circle cx="3" cy="3" r="2.2" fill="#6e9ad6"/><circle cx="14" cy="3" r="2.6" fill="#fff"/><circle cx="26" cy="3" r="2.2" fill="#6e9ad6"/><circle cx="38" cy="3" r="2.2" fill="#6e9ad6"/></svg>
  <div class="soft"></div>
  <div class="abs" style="left:12px;top:335px;font-size:13px;font-weight:600">Assessments</div>
  <div class="tabs"><span class="act">Pending 3</span><span>Completed 4</span></div>
  <div class="a-card" style="top:412px"><div class="kebab"><i></i><i></i><i></i></div>
    <div class="id">1723091983</div><div class="name">Application Design Capabilities</div>
    <div class="dates"><div><small>PUBLISHED ON</small>20/05/2024</div><div><small>DUE DATE</small>24/05/2024</div></div>
    <div class="chips"><span class="chip">Quiz</span><span class="chip">Endorsement</span><span class="chip">Submission</span></div></div>
  <div class="a-card" style="top:567px"><div class="kebab"><i></i><i></i><i></i></div>
    <div class="id">1723091983</div><div class="name">UI/UX Designer Assessments</div>
    <div class="dates"><div><small>PUBLISHED ON</small>20/05/2024</div><div><small>DUE DATE</small>24/05/2024</div></div>
    <div class="chips"><span class="chip">Quiz <i class="tick"></i></span><span class="chip">Endorsement</span></div></div>
  <div class="a-card" style="top:721px"><div class="kebab"><i></i><i></i><i></i></div>
    <div class="id">1723091983</div><div class="name">Sales Representative Assessments</div>
    <div class="dates"><div><small>PUBLISHED ON</small>20/05/2024</div><div><small>DUE DATE</small>24/05/2024</div></div>
    <div class="chips"><span class="chip">Quiz <i class="tick"></i></span><span class="chip">Endorsement <i class="tick"></i></span><span class="chip">Submission</span></div></div>
</section>

<!-- Endorsement screens (3 variants) -->
<section class="screen" style="left:450px;height:1006px">
  <div class="appbar"></div><div class="clock">9:41</div>
  <svg class="bar-icons" width="275" height="80" viewBox="0 0 275 80" aria-hidden="true"><g fill="#fff"><rect x="216" y="15" width="2" height="4"/><rect x="219" y="13" width="2" height="6"/><rect x="222" y="11" width="2" height="8"/><rect x="225" y="9" width="2" height="10"/><path d="M230 12a8 8 0 0 1 10 0l-1.3 1.5a6 6 0 0 0-7.4 0zM232.3 14.7a4.5 4.5 0 0 1 5.4 0L235 18z"/><rect x="244" y="11" width="16" height="7" rx="2"/></g><g stroke="#fff" stroke-width="1.5" fill="none" stroke-linecap="round"><path d="M12 50h15M12 55h11M12 60h15"/><path d="M180 60h12M182 60v-5a4 4 0 0 1 8 0v5M185 63h2"/><circle cx="216" cy="55" r="2.5"/><circle cx="216" cy="55" r="6" stroke-dasharray="3 1.8"/></g></svg>
  <div class="avatar me" role="img" aria-label="User profile photo"></div>
  <div class="crumb"><svg width="15" height="15" viewBox="0 0 15 15" fill="none" stroke="#0e78bb" stroke-width="1.2"><circle cx="7.5" cy="7.5" r="6.5"/><path d="M8.5 4.5l-3 3 3 3M5.5 7.5h4.5"/></svg><b>Assessment</b>/<span>UI/UX Designer Assessment</span></div>
  <div class="head"><svg width="17" height="20" viewBox="0 0 17 20" fill="none" stroke="#4b5360" stroke-width="1.2"><rect x="1" y="2" width="13" height="16" rx="1.5"/><path d="M4 6h7M4 9h4"/><circle cx="10" cy="13" r="2.5"/><path d="M12 15l3 3"/></svg><h1>UI/UX Designer<br>Assessment</h1><div class="pct">80<small>%</small></div></div>
  <div class="meter"><i style="width:205px"></i></div>
  <div class="info">Assessment Date: <span>Feb 12, 2024</span><br>Assessment Type: <span>UI/UX Skill</span><br>Due Date: 17/02/2024<br>Last Updated: 23/05/2024</div>
  <div class="stepper"><i class="dot done"></i><span class="on">Quiz</span><i class="dash"></i><i class="dot"></i><span>Endorsement</span></div>
  <div class="section"><h2>Endorsement</h2><div class="save"><svg width="11" height="11" viewBox="0 0 11 11" fill="none" stroke="#0e78bb" stroke-width="1"><rect x="1" y="1" width="9" height="9" rx="1"/><path d="M3 1v3h5V1M3 10V7h5v3"/></svg>Save Progress</div></div>
  <div class="field dark" style="top:391px">All categories<svg width="8" height="5" viewBox="0 0 8 5" fill="none" stroke="#4b5360"><path d="M1 1l3 3 3-3"/></svg></div>
  <div class="field" style="top:422px">Search<svg width="11" height="11" viewBox="0 0 11 11" fill="none" stroke="#6b7280" stroke-width="1.1"><circle cx="4.5" cy="4.5" r="3.5"/><path d="M7 7l3 3"/></svg></div>
  <div class="send">Send Request</div>
  <div class="row" style="top:493px"><i class="box"></i><div class="avatar" role="img" aria-label="Colleague photo"></div><div class="who">Sora Kim<small>Application Design Capabilities</small></div><div class="add">Add</div></div>
  <div class="row" style="top:533px"><i class="box"></i><div class="avatar" role="img" aria-label="Colleague photo" style="background:#5a5550"></div><div class="who">Owen Hale<small>UI/UX Designer</small></div><div class="add">Add</div></div>
  <div class="row" style="top:572px"><i class="box"></i><div class="avatar" role="img" aria-label="Colleague photo" style="background:#8a8d92"></div><div class="who">Leo Brandt<small>Front-end Developer</small></div><div class="add">Add</div></div>
  <div class="row" style="top:612px"><i class="box"></i><div class="avatar" role="img" aria-label="Colleague photo" style="background:#d6b08a"></div><div class="who">Nina Costa<small>Cybersecurity Analyst</small></div><div class="add">Add</div></div>
  <div class="row" style="top:651px"><i class="box"></i><div class="avatar" role="img" aria-label="Colleague photo" style="background:#7b6f6a"></div><div class="who">Paul Ferris<small>DevOps Engineer</small></div><div class="add">Add</div></div>
  <div class="row" style="top:691px"><i class="box"></i><div class="avatar" role="img" aria-label="Colleague photo" style="background:#a47c54"></div><div class="who">Ivy Marsh<small>DevOps Engineer</small></div><div class="add">Add</div></div>
  <div class="row" style="top:731px"><i class="box"></i><div class="avatar" role="img" aria-label="Colleague photo" style="background:#9aa4ac"></div><div class="who">Dean Pryce<small>DevOps Engineer</small></div><div class="add">Add</div></div>
  <div class="row" style="top:770px"><i class="box"></i><div class="avatar" role="img" aria-label="Colleague photo" style="background:#7a2f2f"></div><div class="who">Rafi Santoso<small>UI Designer</small></div><div class="add">Add</div></div>
  <div class="actions" style="top:822px"><div class="btn-out">Go Back</div><span class="skip">Skip ›</span><div class="btn">Next</div></div>
  <div class="note" style="top:873px;height:110px"><h3>Note</h3>Lorem ipsum dolor sit amet, consecteteur adispiscing elit. Lorem ipsum dolor sit amet, consecteteur adispiscing elit.</div>
</section>

<section class="screen" style="left:798px;height:1006px">
  <div class="appbar"></div><div class="clock">9:41</div>
  <svg class="bar-icons" width="275" height="80" viewBox="0 0 275 80" aria-hidden="true"><g fill="#fff"><rect x="216" y="15" width="2" height="4"/><rect x="219" y="13" width="2" height="6"/><rect x="222" y="11" width="2" height="8"/><rect x="225" y="9" width="2" height="10"/><path d="M230 12a8 8 0 0 1 10 0l-1.3 1.5a6 6 0 0 0-7.4 0zM232.3 14.7a4.5 4.5 0 0 1 5.4 0L235 18z"/><rect x="244" y="11" width="16" height="7" rx="2"/></g><g stroke="#fff" stroke-width="1.5" fill="none" stroke-linecap="round"><path d="M12 50h15M12 55h11M12 60h15"/><path d="M180 60h12M182 60v-5a4 4 0 0 1 8 0v5M185 63h2"/><circle cx="216" cy="55" r="2.5"/><circle cx="216" cy="55" r="6" stroke-dasharray="3 1.8"/></g></svg>
  <div class="avatar me" role="img" aria-label="User profile photo"></div>
  <div class="crumb"><svg width="15" height="15" viewBox="0 0 15 15" fill="none" stroke="#0e78bb" stroke-width="1.2"><circle cx="7.5" cy="7.5" r="6.5"/><path d="M8.5 4.5l-3 3 3 3M5.5 7.5h4.5"/></svg><b>Assessment</b>/<span>UI/UX Designer Assessment</span></div>
  <div class="head"><svg width="17" height="20" viewBox="0 0 17 20" fill="none" stroke="#4b5360" stroke-width="1.2"><rect x="1" y="2" width="13" height="16" rx="1.5"/><path d="M4 6h7M4 9h4"/><circle cx="10" cy="13" r="2.5"/><path d="M12 15l3 3"/></svg><h1>UI/UX Designer<br>Assessment</h1><div class="pct">80<small>%</small></div></div>
  <div class="meter"><i style="width:205px"></i></div>
  <div class="info">Assessment Date: <span>Feb 12, 2024</span><br>Assessment Type: <span>UI/UX Skill</span><br>Due Date: 17/02/2024<br>Last Updated: 23/05/2024</div>
  <div class="stepper"><i class="dot done"></i><span class="on">Quiz</span><i class="dash"></i><i class="dot"></i><span>Endorsement</span></div>
  <div class="section"><h2>Endorsement</h2><div class="save"><svg width="11" height="11" viewBox="0 0 11 11" fill="none" stroke="#0e78bb" stroke-width="1"><rect x="1" y="1" width="9" height="9" rx="1"/><path d="M3 1v3h5V1M3 10V7h5v3"/></svg>Save Progress</div></div>
  <div class="field dark" style="top:391px">All categories<svg width="8" height="5" viewBox="0 0 8 5" fill="none" stroke="#4b5360"><path d="M1 1l3 3 3-3"/></svg></div>
  <div class="field" style="top:422px">Search<svg width="11" height="11" viewBox="0 0 11 11" fill="none" stroke="#6b7280" stroke-width="1.1"><circle cx="4.5" cy="4.5" r="3.5"/><path d="M7 7l3 3"/></svg></div>
  <div class="send live">Send Request</div>
  <div class="row" style="top:493px"><i class="box"></i><div class="avatar" role="img" aria-label="Colleague photo"></div><div class="who">Sora Kim<small>Application Design Capabilities</small></div><div class="add">Add</div></div>
  <div class="row" style="top:533px"><i class="box"></i><div class="avatar" role="img" aria-label="Colleague photo" style="background:#5a5550"></div><div class="who">Owen Hale<small>UI/UX Designer</small></div><div class="add">Add</div></div>
  <div class="row" style="top:572px"><i class="box"></i><div class="avatar" role="img" aria-label="Colleague photo" style="background:#8a8d92"></div><div class="who">Leo Brandt<small>Front-end Developer</small></div><div class="add">Add</div></div>
  <div class="row" style="top:612px"><i class="box"></i><div class="avatar" role="img" aria-label="Colleague photo" style="background:#d6b08a"></div><div class="who">Nina Costa<small>Cybersecurity Analyst</small></div><div class="add">Add</div></div>
  <div class="row" style="top:651px"><i class="box on"></i><div class="avatar" role="img" aria-label="Colleague photo" style="background:#7b6f6a"></div><div class="who">Paul Ferris<small>DevOps Engineer</small></div><div class="add">Add</div></div>
  <div class="row" style="top:691px"><i class="box on"></i><div class="avatar" role="img" aria-label="Colleague photo" style="background:#a47c54"></div><div class="who">Ivy Marsh<small>DevOps Engineer</small></div><div class="add">Add</div></div>
  <div class="row" style="top:731px"><i class="box"></i><div class="avatar" role="img" aria-label="Colleague photo" style="background:#9aa4ac"></div><div class="who">Dean Pryce<small>DevOps Engineer</small></div><div class="add">Add</div></div>
  <div class="row" style="top:770px"><i class="box"></i><div class="avatar" role="img" aria-label="Colleague photo" style="background:#7a2f2f"></div><div class="who">Rafi Santoso<small>UI Designer</small></div><div class="add">Add</div></div>
  <div class="actions" style="top:822px"><div class="btn-out">Go Back</div><span class="skip">Skip ›</span><div class="btn">Next</div></div>
  <div class="note" style="top:873px;height:110px"><h3>Note</h3>Lorem ipsum dolor sit amet, consecteteur adispiscing elit. Lorem ipsum dolor sit amet, consecteteur adispiscing elit.</div>
</section>

<section class="screen" style="left:1147px;height:1006px">
  <div class="appbar"></div><div class="clock">9:41</div>
  <svg class="bar-icons" width="275" height="80" viewBox="0 0 275 80" aria-hidden="true"><g fill="#fff"><rect x="216" y="15" width="2" height="4"/><rect x="219" y="13" width="2" height="6"/><rect x="222" y="11" width="2" height="8"/><rect x="225" y="9" width="2" height="10"/><path d="M230 12a8 8 0 0 1 10 0l-1.3 1.5a6 6 0 0 0-7.4 0zM232.3 14.7a4.5 4.5 0 0 1 5.4 0L235 18z"/><rect x="244" y="11" width="16" height="7" rx="2"/></g><g stroke="#fff" stroke-width="1.5" fill="none" stroke-linecap="round"><path d="M12 50h15M12 55h11M12 60h15"/><path d="M180 60h12M182 60v-5a4 4 0 0 1 8 0v5M185 63h2"/><circle cx="216" cy="55" r="2.5"/><circle cx="216" cy="55" r="6" stroke-dasharray="3 1.8"/></g></svg>
  <div class="avatar me" role="img" aria-label="User profile photo"></div>
  <div class="crumb"><svg width="15" height="15" viewBox="0 0 15 15" fill="none" stroke="#0e78bb" stroke-width="1.2"><circle cx="7.5" cy="7.5" r="6.5"/><path d="M8.5 4.5l-3 3 3 3M5.5 7.5h4.5"/></svg><b>Assessment</b>/<span>UI/UX Designer Assessment</span></div>
  <div class="head"><svg width="17" height="20" viewBox="0 0 17 20" fill="none" stroke="#4b5360" stroke-width="1.2"><rect x="1" y="2" width="13" height="16" rx="1.5"/><path d="M4 6h7M4 9h4"/><circle cx="10" cy="13" r="2.5"/><path d="M12 15l3 3"/></svg><h1>UI/UX Designer<br>Assessment</h1><div class="pct">80<small>%</small></div></div>
  <div class="meter"><i style="width:205px"></i></div>
  <div class="info">Assessment Date: <span>Feb 12, 2024</span><br>Assessment Type: <span>UI/UX Skill</span><br>Due Date: 17/02/2024<br>Last Updated: 23/05/2024</div>
  <div class="stepper"><i class="dot done"></i><span class="on">Quiz</span><i class="dash"></i><i class="dot"></i><span>Endorsement</span></div>
  <div class="section"><h2>Endorsement</h2><div class="save"><svg width="11" height="11" viewBox="0 0 11 11" fill="none" stroke="#0e78bb" stroke-width="1"><rect x="1" y="1" width="9" height="9" rx="1"/><path d="M3 1v3h5V1M3 10V7h5v3"/></svg>Save Progress</div></div>
  <div class="row" style="top:612px"><i class="box"></i><div class="avatar" role="img" aria-label="Colleague photo" style="background:#d6b08a"></div><div class="who">Nina Costa<small>Cybersecurity Analyst</small></div><div class="add">Add</div></div>
  <div class="row" style="top:651px"><i class="box on"></i><div class="avatar" role="img" aria-label="Colleague photo" style="background:#7b6f6a"></div><div class="who">Paul Ferris<small>DevOps Engineer</small></div><div class="add">Add</div></div>
  <div class="row" style="top:691px"><i class="box on"></i><div class="avatar" role="img" aria-label="Colleague photo" style="background:#a47c54"></div><div class="who">Ivy Marsh<small>DevOps Engineer</small></div><div class="add">Add</div></div>
  <div class="row" style="top:731px"><i class="box"></i><div class="avatar" role="img" aria-label="Colleague photo" style="background:#9aa4ac"></div><div class="who">Dean Pryce<small>DevOps Engineer</small></div><div class="add">Add</div></div>
  <div class="row" style="top:770px"><i class="box"></i><div class="avatar" role="img" aria-label="Colleague photo" style="background:#7a2f2f"></div><div class="who">Rafi Santoso<small>UI Designer</small></div><div class="add">Add</div></div>
  <div class="actions" style="top:822px"><div class="btn-out">Go Back</div><span class="skip">Skip ›</span><div class="btn">Next</div></div>
  <div class="note" style="top:873px;height:110px"><h3>Note</h3>Lorem ipsum dolor sit amet, consecteteur adispiscing elit. Lorem ipsum dolor sit amet, consecteteur adispiscing elit.</div>
  <div class="dim"></div>
  <div class="modal">
    <h4>Endorsements</h4>
    <div class="avatar abs" role="img" aria-label="Selected colleague photo" style="left:23px;top:62px;width:22px;height:22px;background:#7b6f6a"></div>
    <div class="avatar abs" role="img" aria-label="Selected colleague photo" style="left:53px;top:62px;width:22px;height:22px;background:#a47c54"></div>
    <div class="abs" style="left:23px;top:98px;font-size:7.5px;color:var(--muted)">You will add <b style="color:var(--ink)">2</b> colleagues to endorsement you.</div>
    <div class="abs" style="left:23px;top:127px;font-size:7.5px;color:#4b5360">Effective Date</div>
    <div class="field dark" style="left:23px;top:143px;width:205px;font-size:8.5px">Select date<svg width="8" height="5" viewBox="0 0 8 5" fill="none" stroke="#4b5360"><path d="M1 1l3 3 3-3"/></svg></div>
    <div class="abs btn-out" style="left:23px;top:187px;width:56px;font-size:9px">Cancel</div>
    <div class="abs btn" style="left:172px;top:187px;width:56px;font-size:9px">Submit</div>
  </div>
</section>

<!-- Quiz: multiple choice -->
<section class="screen" style="left:1495px;height:945px">
  <div class="appbar"></div><div class="clock">9:41</div>
  <svg class="bar-icons" width="275" height="80" viewBox="0 0 275 80" aria-hidden="true"><g fill="#fff"><rect x="216" y="15" width="2" height="4"/><rect x="219" y="13" width="2" height="6"/><rect x="222" y="11" width="2" height="8"/><rect x="225" y="9" width="2" height="10"/><path d="M230 12a8 8 0 0 1 10 0l-1.3 1.5a6 6 0 0 0-7.4 0zM232.3 14.7a4.5 4.5 0 0 1 5.4 0L235 18z"/><rect x="244" y="11" width="16" height="7" rx="2"/></g><g stroke="#fff" stroke-width="1.5" fill="none" stroke-linecap="round"><path d="M12 50h15M12 55h11M12 60h15"/><path d="M180 60h12M182 60v-5a4 4 0 0 1 8 0v5M185 63h2"/><circle cx="216" cy="55" r="2.5"/><circle cx="216" cy="55" r="6" stroke-dasharray="3 1.8"/></g></svg>
  <div class="avatar me" role="img" aria-label="User profile photo"></div>
  <div class="crumb"><svg width="15" height="15" viewBox="0 0 15 15" fill="none" stroke="#0e78bb" stroke-width="1.2"><circle cx="7.5" cy="7.5" r="6.5"/><path d="M8.5 4.5l-3 3 3 3M5.5 7.5h4.5"/></svg><b>Assessment</b>/<span>UI/UX Designer Assessment</span></div>
  <div class="head"><svg width="17" height="20" viewBox="0 0 17 20" fill="none" stroke="#4b5360" stroke-width="1.2"><rect x="1" y="2" width="13" height="16" rx="1.5"/><path d="M4 6h7M4 9h4"/><circle cx="10" cy="13" r="2.5"/><path d="M12 15l3 3"/></svg><h1>Application Design<br>Capabilities</h1><div class="pct">20<small>%</small></div></div>
  <div class="meter"><i style="width:55px"></i></div>
  <div class="info">Assessment Date: <span>May 20, 2024</span><br>Assessment Type: <span>UI/UX Skill</span><br>Due Date: 24/05/2024<br>Last Updated: 23/05/2024</div>
  <div class="stepper"><i class="dot"></i><span class="on">Quiz</span><i class="dash"></i><i class="dot"></i><span>Endorsement</span><i class="dash"></i><i class="dot"></i><span>Submissions</span></div>
  <div class="section"><h2>Quiz</h2><div class="save"><svg width="11" height="11" viewBox="0 0 11 11" fill="none" stroke="#0e78bb" stroke-width="1"><rect x="1" y="1" width="9" height="9" rx="1"/><path d="M3 1v3h5V1M3 10V7h5v3"/></svg>Save Progress</div></div>
  <div class="progress-line"><svg width="5" height="8" viewBox="0 0 5 8" fill="none" stroke="#4b5360"><path d="M1 1l3 3-3 3"/></svg>Progress<svg class="ring" width="24" height="24" viewBox="0 0 24 24" fill="none" stroke-width="2.5"><circle cx="12" cy="12" r="10" stroke="#e3e6eb"/><circle cx="12" cy="12" r="10" stroke="#0e78bb" stroke-dasharray="39.3 62.8" transform="rotate(-90 12 12)"/></svg><span class="count"><b style="color:var(--ink)">5</b> / 8</span></div>
  <div class="q" style="top:429px"><span class="no">Q.5.</span><span>What's your knowledge regarding User Interface?</span></div>
  <div class="opt" style="top:477px"><span class="n">1</span>Lorem ipsum dolor sit amet,<br>consecteteur adispiscing elit.</div>
  <div class="opt" style="top:536px"><span class="n">2</span>Lorem ipsum dolor sit amet,<br>consecteteur adispiscing elit.</div>
  <div class="opt sel" style="top:594px"><span class="n">3</span>Lorem ipsum dolor sit amet,<br>consecteteur adispiscing elit.</div>
  <div class="opt" style="top:653px"><span class="n">4</span>Lorem ipsum dolor sit amet,<br>consecteteur adispiscing elit.</div>
  <div class="actions" style="top:743px"><div class="btn-out">Go Back</div><span class="skip">Skip ›</span><div class="btn">Next</div></div>
  <div class="note" style="top:793px;height:127px"><h3>Note</h3>Lorem ipsum dolor sit amet, consecteteur adispiscing elit. Lorem ipsum dolor sit amet, consecteteur adispiscing elit.Lorem ipsum dolor sit amet, consecteteur adispiscing elit.</div>
</section>

<!-- Quiz: true / false -->
<section class="screen" style="left:1844px;height:707px">
  <div class="appbar"></div><div class="clock">9:41</div>
  <svg class="bar-icons" width="275" height="80" viewBox="0 0 275 80" aria-hidden="true"><g fill="#fff"><rect x="216" y="15" width="2" height="4"/><rect x="219" y="13" width="2" height="6"/><rect x="222" y="11" width="2" height="8"/><rect x="225" y="9" width="2" height="10"/><path d="M230 12a8 8 0 0 1 10 0l-1.3 1.5a6 6 0 0 0-7.4 0zM232.3 14.7a4.5 4.5 0 0 1 5.4 0L235 18z"/><rect x="244" y="11" width="16" height="7" rx="2"/></g><g stroke="#fff" stroke-width="1.5" fill="none" stroke-linecap="round"><path d="M12 50h15M12 55h11M12 60h15"/><path d="M180 60h12M182 60v-5a4 4 0 0 1 8 0v5M185 63h2"/><circle cx="216" cy="55" r="2.5"/><circle cx="216" cy="55" r="6" stroke-dasharray="3 1.8"/></g></svg>
  <div class="avatar me" role="img" aria-label="User profile photo"></div>
  <div class="crumb"><svg width="15" height="15" viewBox="0 0 15 15" fill="none" stroke="#0e78bb" stroke-width="1.2"><circle cx="7.5" cy="7.5" r="6.5"/><path d="M8.5 4.5l-3 3 3 3M5.5 7.5h4.5"/></svg><b>Assessment</b>/<span>UI/UX Designer Assessment</span></div>
  <div class="head"><svg width="17" height="20" viewBox="0 0 17 20" fill="none" stroke="#4b5360" stroke-width="1.2"><rect x="1" y="2" width="13" height="16" rx="1.5"/><path d="M4 6h7M4 9h4"/><circle cx="10" cy="13" r="2.5"/><path d="M12 15l3 3"/></svg><h1>Application Design<br>Capabilities</h1><div class="pct">35<small>%</small></div></div>
  <div class="meter"><i style="width:96px"></i></div>
  <div class="info">Assessment Date: <span>May 20, 2024</span><br>Assessment Type: <span>UI/UX Skill</span><br>Due Date: 24/05/2024<br>Last Updated: 23/05/2024</div>
  <div class="stepper"><i class="dot"></i><span class="on">Quiz</span><i class="dash"></i><i class="dot"></i><span>Endorsement</span><i class="dash"></i><i class="dot"></i><span>Submissions</span></div>
  <div class="section"><h2>Quiz</h2><div class="save"><svg width="11" height="11" viewBox="0 0 11 11" fill="none" stroke="#0e78bb" stroke-width="1"><rect x="1" y="1" width="9" height="9" rx="1"/><path d="M3 1v3h5V1M3 10V7h5v3"/></svg>Save Progress</div></div>
  <div class="progress-line"><svg width="5" height="8" viewBox="0 0 5 8" fill="none" stroke="#4b5360"><path d="M1 1l3 3-3 3"/></svg>Progress<svg class="ring" width="24" height="24" viewBox="0 0 24 24" fill="none" stroke-width="2.5"><circle cx="12" cy="12" r="10" stroke="#e3e6eb"/><circle cx="12" cy="12" r="10" stroke="#0e78bb" stroke-dasharray="55 62.8" transform="rotate(-90 12 12)"/></svg><span class="count"><b style="color:var(--ink)">7</b> / 8</span></div>
  <div class="q" style="top:429px"><span class="no">Q.5.</span><span>This is a single question with T/F choice</span></div>
  <div class="pill" style="left:54px;width:45px;background:var(--primary);color:#fff;border:1px solid var(--primary)">True</div>
  <div class="pill" style="left:104px;width:47px;border:1px solid var(--line);color:var(--primary)">False</div>
  <div class="actions" style="top:541px"><div class="btn-out">Go Back</div><span class="skip">Skip ›</span><div class="btn">Next</div></div>
  <div class="note" style="top:593px;height:90px"><h3>Note</h3>Lorem ipsum dolor sit amet, consecteteur adispiscing elit. Lorem ipsum dolor sit amet</div>
</section>

<!-- Quiz: fill in the blanks -->
<section class="screen" style="left:2192px;height:813px">
  <div class="appbar"></div><div class="clock">9:41</div>
  <svg class="bar-icons" width="275" height="80" viewBox="0 0 275 80" aria-hidden="true"><g fill="#fff"><rect x="216" y="15" width="2" height="4"/><rect x="219" y="13" width="2" height="6"/><rect x="222" y="11" width="2" height="8"/><rect x="225" y="9" width="2" height="10"/><path d="M230 12a8 8 0 0 1 10 0l-1.3 1.5a6 6 0 0 0-7.4 0zM232.3 14.7a4.5 4.5 0 0 1 5.4 0L235 18z"/><rect x="244" y="11" width="16" height="7" rx="2"/></g><g stroke="#fff" stroke-width="1.5" fill="none" stroke-linecap="round"><path d="M12 50h15M12 55h11M12 60h15"/><path d="M180 60h12M182 60v-5a4 4 0 0 1 8 0v5M185 63h2"/><circle cx="216" cy="55" r="2.5"/><circle cx="216" cy="55" r="6" stroke-dasharray="3 1.8"/></g></svg>
  <div class="avatar me" role="img" aria-label="User profile photo"></div>
  <div class="crumb"><svg width="15" height="15" viewBox="0 0 15 15" fill="none" stroke="#0e78bb" stroke-width="1.2"><circle cx="7.5" cy="7.5" r="6.5"/><path d="M8.5 4.5l-3 3 3 3M5.5 7.5h4.5"/></svg><b>Assessment</b>/<span>UI/UX Designer Assessment</span></div>
  <div class="head"><svg width="17" height="20" viewBox="0 0 17 20" fill="none" stroke="#4b5360" stroke-width="1.2"><rect x="1" y="2" width="13" height="16" rx="1.5"/><path d="M4 6h7M4 9h4"/><circle cx="10" cy="13" r="2.5"/><path d="M12 15l3 3"/></svg><h1>Application Design<br>Capabilities</h1><div class="pct">50<small>%</small></div></div>
  <div class="meter"><i style="width:138px"></i></div>
  <div class="info">Assessment Date: <span>May 20, 2024</span><br>Assessment Type: <span>UI/UX Skill</span><br>Due Date: 24/05/2024<br>Last Updated: 23/05/2024</div>
  <div class="stepper"><i class="dot"></i><span class="on">Quiz</span><i class="dash"></i><i class="dot"></i><span>Endorsement</span><i class="dash"></i><i class="dot"></i><span>Submissions</span></div>
  <div class="section"><h2>Quiz</h2><div class="save"><svg width="11" height="11" viewBox="0 0 11 11" fill="none" stroke="#0e78bb" stroke-width="1"><rect x="1" y="1" width="9" height="9" rx="1"/><path d="M3 1v3h5V1M3 10V7h5v3"/></svg>Save Progress</div></div>
  <div class="progress-line"><svg width="5" height="8" viewBox="0 0 5 8" fill="none" stroke="#4b5360"><path d="M1 1l3 3-3 3"/></svg>Progress<svg class="ring" width="24" height="24" viewBox="0 0 24 24" fill="none" stroke-width="2.5"><circle cx="12" cy="12" r="10" stroke="#0e78bb"/></svg><span class="count"><b style="color:var(--ink)">8</b> / 8</span></div>
  <div class="abs" style="left:12px;top:429px;font-size:12.5px;color:#4b5360">Q.5.</div>
  <div class="blank-text" style="top:429px">How do you</div>
  <div class="blank" style="left:139px;top:429px;width:124px">Type a label</div>
  <div class="blank-text" style="top:469px">This is a fill in the</div>
  <div class="blank" style="left:174px;top:469px;width:89px">blanks</div>
  <div class="blank-text" style="top:508px">field. Please</div>
  <div class="blank-text" style="top:542px">sign your name:</div>
  <div class="blank" style="left:160px;top:542px;width:103px">here</div>
  <div class="blank-text" style="top:580px">. Thank you</div>
  <div class="actions" style="top:632px"><div class="btn-out">Go Back</div><span class="skip">Skip ›</span><div class="btn">Next</div></div>
  <div class="note" style="top:683px;height:109px"><h3>Note</h3>Lorem ipsum dolor sit amet, consecteteur adispiscing elit. Lorem ipsum dolor sit amet, consecteteur adispiscing.</div>
</section>
</div>
</body></html>
```